Brochure design for Velicor

Create a bi-fold A5 size brochure. I have attached our logo and the written content to be included in the brochure. So the brochure will have a total of 4 pages (front page, inner two pages, back page). End source files need to include final printable brochure as well as editable files.

```html
<!DOCTYPE html>
<html lang="en">
<head>
<meta charset="utf-8">
<title>Velicor Brochure – Spreads</title>
<link href="https://fonts.googleapis.com/css2?family=Open+Sans:wght@400;600;700&family=Arimo:wght@400;700&display=swap" rel="stylesheet">
<style>
  :root{
    --stage:#4d4d4d;
    --navy:#0f3868;
    --blue:#1a5a9a;
    --teal:#1b6e78;
    --green:#8dc63f;
    --green-dark:#2e7d4f;
    --brand-blue:#1f5fa0;
    --ink:#2a2a2a;
    --white:#ffffff;
    --paper:#f4f5f6;
  }
  *{box-sizing:border-box;margin:0;padding:0}
  html,body{width:1200px;height:1200px;overflow:hidden;background:var(--white)}
  body{font-family:"Open Sans",Arial,sans-serif;position:relative}
  .stage{position:absolute;left:94px;top:0;width:1000px;height:1200px;background:var(--stage)}
  .page{position:absolute;overflow:hidden;box-shadow:0 6px 14px rgba(0,0,0,.45)}
  .abs{position:absolute}

  /* back cover */
  .back-cover{left:225px;top:51px;width:378px;height:536px;
    background:linear-gradient(150deg,#1d6a6e 0%,#13497a 45%,#0f3868 100%);color:var(--white)}
  .contact{left:24px;top:35px;width:330px;text-align:center;font-size:7.8px;line-height:10.4px}
  .contact p{margin-bottom:2.6px}
  .contact .link{color:var(--green)}
  .contact-rule{left:114px;top:116px;width:150px;height:1px;background:rgba(255,255,255,.8)}
  .wordmark{display:flex;align-items:center;gap:6px;font-family:"Open Sans",Arial,sans-serif;font-weight:600}
  .wordmark .dot{border-radius:50%;display:inline-block}
  .back-cover .wordmark{left:0;width:378px;top:235px;justify-content:center;font-size:23px;color:var(--white)}
  .back-cover .wordmark .dot{width:14px;height:14px;background:var(--white)}
  .references{left:27px;top:344px;width:335px;font-size:6px;line-height:7.4px}
  .references h4{color:var(--green);font-size:8.6px;font-weight:400;margin-bottom:5px}
  .references ol{padding-left:10px}
  .references li{margin-bottom:1.8px}
  .references .note{font-style:italic;padding-left:10px}

  /* front cover */
  .front-cover{left:603px;top:51px;width:374px;height:536px;background:var(--white)}
  .front-cover .wordmark{left:48px;top:50px;font-size:44px;color:var(--brand-blue);letter-spacing:-.5px}
  .front-cover .wordmark .dot{width:34px;height:34px;background:var(--green)}
  .cover-photo{left:0;top:120px;width:374px;height:333px;
    background:radial-gradient(ellipse at 65% 40%,#e9f0f8 0%,#cfdeef 45%,#a8c3e2 100%)}
  .cover-band{left:0;top:453px;width:374px;height:57px;
    background:linear-gradient(90deg,var(--green-dark),#1d6570 60%,#184f6e);
    text-align:center;font-family:"Arimo",Arial,sans-serif;font-size:19px;line-height:21px;padding-top:7px}
  .cover-band .lead{color:var(--green)}
  .cover-band .main{color:var(--white)}

  /* inner left */
  .inner-left{left:225px;top:615px;width:378px;height:540px;
    background:linear-gradient(165deg,#1e7460 0%,#1a5d78 35%,#134e86 70%,#10427a 100%);color:var(--white)}
  .inner-heading{right:33px;top:27px;text-align:right;font-family:"Arimo",Arial,sans-serif;font-size:16px;line-height:21px;z-index:2}
  .inner-heading .hl{color:var(--green);font-weight:700}
  .diag-band{left:60px;top:118px;width:260px;height:34px;background:rgba(141,198,63,.35);transform:rotate(22deg);transform-origin:left center}
  .photo-ring{border-radius:50%;background:#1b6f86;box-shadow:0 0 0 3px #178a9c}
  .photo{border-radius:50%}
  .ring-runner{left:15px;top:36px;width:130px;height:130px}
  .photo-runner{left:22px;top:43px;width:116px;height:116px;background:radial-gradient(circle at 60% 40%,#f6d9a8,#d98a4e 60%,#6d5a4c)}
  .ring-family{left:211px;top:126px;width:128px;height:128px}
  .photo-family{left:218px;top:133px;width:114px;height:114px;background:radial-gradient(circle at 50% 40%,#e8efe0,#b7c98a 55%,#6f8f3f)}
  .section{left:35px;width:310px;font-size:7.6px;line-height:9.3px}
  .sec-head{display:flex;align-items:flex-end;gap:8px;font-size:9.4px;line-height:11px;margin-bottom:6px}
  .sec-head .hl{color:var(--green);font-weight:600}
  .spacer{float:right;width:118px;height:46px}
  .s-precision{top:184px}
  .s-dna{top:303px}
  .s-unlock{top:426px}

  /* inner right */
  .inner-right{left:603px;top:615px;width:377px;height:540px;
    background:linear-gradient(180deg,#f7f8f9,#eceef0);color:var(--ink)}
  .top-bar{left:0;top:28px;width:224px;height:6px;background:linear-gradient(90deg,#1d6570,var(--green-dark))}
  .inner-right .wordmark{left:258px;top:14px;font-size:19px;color:var(--brand-blue)}
  .inner-right .wordmark .dot{width:16px;height:16px;background:var(--green)}
  .topic{left:27px;width:331px;font-size:7.4px;line-height:9.4px;text-align:justify}
  .topic .sec-head{color:#333;font-size:9.4px;margin-left:4px}
  .topic .sec-head .hl{color:var(--brand-blue);font-weight:700}
  .t-disease{top:52px}
  .t-drugs{top:176px}
  .t-diet{top:312px}
  .t-descent{top:425px}
  .bottom-bar{left:0;top:533px;width:377px;height:7px;background:var(--green)}
</style>
</head>
<body>
<div class="stage"></div>

<!-- Outer spread -->
<section class="page back-cover">
  <div class="abs contact">
    <p>For more information about VelicorTM or our products, please talk to your local retailer or email us at <span class="link">enquiries@velicor.co</span></p>
    <p>Please note test availability may differ from region to region and is subject to availability. Please talk to your local retailer for more information.</p>
    <p>For a list of approved VelicorTM retailers please visit <span class="link">www.velicor.co</span></p>
  </div>
  <div class="abs contact-rule"></div>
  <div class="abs wordmark"><span class="dot"></span>Velicor</div>
  <div class="abs references">
    <h4>References:</h4>
    <ol>
      <li>Sequencing consortium. Complete genome release. Public archive, 2003.</li>
      <li>Author A, et al. Clinical use of pharmacogenetics. Review 7:201-204.</li>
      <li>Author B, et al. Pharmacogenetics overview. 1998;8:283-289.</li>
      <li>Author C, et al. Molecular diagnostics journal 2016;18:438-45.</li>
      <li>Author D, et al. Clinical pharmacology and therapeutics 2016;100:160-9.</li>
      <li>Author E, et al. Personalized medicine review 2017;27:17-27.</li>
      <li>Author F, et al. Clinical pharmacology report 2014;95:423-31.</li>
      <li>Author G, et al. Food elimination and bowel symptoms: a randomised controlled trial. Gut journal 2004;53:1459-1464.</li>
      <li>Author H, et al. Randomised trial of elimination diet for prevention of migraine headaches. Nutrition journal 2011;10:85.</li>
      <li>Author J, et al. Food allergy and migraine in adults. Allergy review 2007;54:162-8.</li>
      <li>Author K, et al. Immune complexes in food-induced arthralgia. Allergy 1987;59:422-8.</li>
    </ol>
    <p class="note">* Additional fees may apply.</p>
  </div>
</section>

<section class="page front-cover">
  <div class="abs wordmark"><span class="dot"></span>Velicor</div>
  <div class="abs cover-photo" role="img" aria-label="Doctor with stethoscope touching a hexagon health interface with genetic testing, DNA, sequencing and health icons"></div>
  <div class="abs cover-band">
    <div class="lead">WE'RE HELPING TO BUILD</div>
    <div class="main">THE FUTURE OF GOOD HEALTH</div>
  </div>
</section>

<!-- Inner spread -->
<section class="page inner-left">
  <div class="abs diag-band"></div>
  <div class="abs photo-ring ring-runner"></div>
  <div class="abs photo photo-runner" role="img" aria-label="Woman running along a seaside boardwalk at sunset"></div>
  <div class="abs photo-ring ring-family"></div>
  <div class="abs photo photo-family" role="img" aria-label="Happy family playing together on the grass"></div>
  <div class="abs inner-heading">
    PRECISION HEALTH AND<br>WELLNESS IS TAILORED<br><span class="hl">TO YOUR UNIQUE<br>GENETIC MAKE-UP</span>
  </div>

  <div class="abs section s-precision">
    <div class="sec-head">
      <svg width="32" height="30" viewBox="0 0 32 30" aria-hidden="true"><rect x="2" y="2" width="18" height="24" rx="2" fill="none" stroke="#8dc63f" stroke-width="2"/><path d="M8 9h6M11 6v6M6 17h10M6 21h8" stroke="#8dc63f" stroke-width="1.8"/><path d="M22 14l7 2v5c0 4-3 6-7 8-4-2-7-4-7-8v-5z" fill="#8dc63f"/><path d="M19 21l2 2 4-4" stroke="#fff" stroke-width="1.6" fill="none"/></svg>
      <div>PRECISION<br><span class="hl">HEALTH &amp; WELLNESS</span></div>
    </div>
    <p><span class="spacer"></span>You are unique. Your healthcare and lifestyle decisions need to be tailored to you. Ever since the human genome was decoded, a plethora of scientific data has revealed everything from disease-causing genes to genetically tailored diets. We all want to live longer and healthier lives, whilst performing at out peak. One size does not fit all and the only way to find out what's right for you is to unlock your hidden code.</p>
  </div>

  <div class="abs section s-dna">
    <div class="sec-head">
      <svg width="20" height="34" viewBox="0 0 20 34" aria-hidden="true"><path d="M4 2c0 8 12 8 12 15S4 24 4 32M16 2c0 8-12 8-12 15s12 7 12 15" stroke="#8dc63f" stroke-width="2" fill="none"/><path d="M6 6h8M6 12h8M6 22h8M6 28h8" stroke="#8dc63f" stroke-width="1.4"/></svg>
      <div>DNA - <span class="hl">THE CODE OF LIFE</span></div>
    </div>
    <p>Every individual living organism has a completely unique set of DNA. Your DNA is the chemical blueprint that codes for everything in your body and is found in all of the trillions of cells that you are made of. Collections of DNA are called genes and the complete set of genes in an individual is referred to as their genome. The human genome was first decoded in 2003, taking over 13 years and $2.7 billion to complete1. Thanks to exponential advances in technology, VelicorTM can now unlock your DNA for only a fraction of the time and cost.</p>
  </div>

  <div class="abs section s-unlock">
    <div class="sec-head">
      <svg width="22" height="32" viewBox="0 0 22 32" aria-hidden="true"><path d="M5 14V8a6 6 0 0 1 12 0" stroke="#8dc63f" stroke-width="3" fill="none"/><rect x="1" y="14" width="20" height="17" rx="3" fill="#8dc63f"/><circle cx="11" cy="22" r="2.5" fill="#1a5d78"/></svg>
      <div>UNLOCK <span class="hl">YOUR HIDDEN CODE</span></div>
    </div>
    <p>A whole new world of discovery awaits with the VelicorTM range of genetic testing services. From unlocking your complete genome with Whole Genome Sequencing (WGS) to just learning about specific aspects of what makes you... you. With VelicorTM, you can find answers to the questions that can help you to live a healthier, longer and optimal quality of life.</p>
  </div>
</section>

<section class="page inner-right">
  <div class="abs top-bar"></div>
  <div class="abs wordmark"><span class="dot"></span>Velicor</div>

  <div class="abs topic t-disease">
    <div class="sec-head">
      <svg width="30" height="28" viewBox="0 0 30 28" aria-hidden="true"><path d="M4 26c2-8 4-12 11-12s9 4 11 12" stroke="#1f5fa0" stroke-width="1.6" fill="none"/><circle cx="15" cy="9" r="5" fill="none" stroke="#1f5fa0" stroke-width="1.6"/><path d="M13 2v3M17 2v3" stroke="#1f5fa0" stroke-width="1.2"/></svg>
      <div>DNA <span class="hl">&amp; DISEASE</span></div>
    </div>
    <p>Prevention is better than any cure. Scientific studies have uncovered numerous genes associated with a range of cancers, heart conditions, and other common diseases affecting society today. The range of genetic tests available through VelicorTM can now identify if these, and other, genes are present in you. This allows you and your physician to potentially prevent, manage, monitor and treat relevant conditions. Furthermore, as the rapid pace of science continues to uncover new genes related to disease, VelicorTM can quickly update you and your doctor with the latest research and what it means for you*.</p>
  </div>

  <div class="abs topic t-drugs">
    <div class="sec-head">
      <svg width="34" height="22" viewBox="0 0 34 22" aria-hidden="true"><rect x="2" y="2" width="9" height="18" rx="4.5" fill="none" stroke="#1f5fa0" stroke-width="1.8"/><path d="M2 11h9" stroke="#1f5fa0" stroke-width="1.8"/><rect x="15" y="8" width="17" height="9" rx="4.5" fill="#1f5fa0"/></svg>
      <div>DNA <span class="hl">&amp; DRUGS</span></div>
    </div>
    <p>Scientific research has shown that the response rate for many prescribed drugs is as low as 50% and that genetic factors can account for up to 95% of drug-response variability and susceptibility.2-3 In other words, many of the drugs you take in your lifetime will likely be inadequately dosed, leading to potential side effects or no effects at all. With VelicorTM, you and your doctor can proactively identify appropriate types, and dosages, for a range of prescribed and over-the-counter medications. This includes medications you currently take and any commons future medications you are likely to encounter at some stage in your life. A number of studies have shown that over 74% of people taking a genetic test for medication compatibility learned information that is relevant to them.4-7</p>
  </div>

  <div class="abs topic t-diet">
    <div class="sec-head">
      <svg width="30" height="30" viewBox="0 0 30 30" aria-hidden="true"><rect x="3" y="3" width="18" height="24" rx="2" fill="none" stroke="#1f5fa0" stroke-width="1.8"/><path d="M7 9h10M7 14h10M7 19h7" stroke="#1f5fa0" stroke-width="1.4"/><circle cx="23" cy="23" r="5" fill="#fff" stroke="#1f5fa0" stroke-width="1.6"/></svg>
      <div>DNA <span class="hl">&amp; DIET</span></div>
    </div>
    <p>Certain foods are thought to inappropriately cause immune reactions in genetically predisposed individuals. This can result in symptoms like fatigue, bloating, bowel disturbances, headaches, migraines, joint aches, eczema or acne8-11. DNA testing can help identify such foods as well as genes associated with the metabolism and absorption of vitamins, minerals and stimulants like coffee. The VelicorTM range of tests can even help create precision diet and fitness plans based on your genes and goals.</p>
  </div>

  <div class="abs topic t-descent">
    <div class="sec-head">
      <svg width="32" height="28" viewBox="0 0 32 28" aria-hidden="true"><path d="M16 8v8M16 16L6 23M16 16l10 7" stroke="#1f5fa0" stroke-width="2"/><circle cx="16" cy="6" r="4" fill="#1f5fa0"/><circle cx="16" cy="16" r="3.5" fill="#1f5fa0"/><circle cx="5" cy="23" r="4" fill="#1f5fa0"/><circle cx="27" cy="23" r="4" fill="#1f5fa0"/></svg>
      <div>DNA <span class="hl">&amp; DESCENT</span></div>
    </div>
    <p>The discipline of genealogy has exploded over recent years with the advent of DNA testing. The VelicorTM range of tests can help you track and understand your ancestry and paternity tests can help identify an individual's biological father. Family planning tests can help identify a couple's risk profile for conceiving children with any of the dozens of known genetic conditions that can affect humans.</p>
  </div>

  <div class="abs bottom-bar"></div>
</section>
</body>
</html>
```